BRC Trifold

- Hello -
We are looking for an exciting trifold design for our residential roofing and interior remodeling company. Below is the website for more inspiration and images. We would like to include the Veteran Owned section somewhere on the back.

https://brellmontroofingandconstruction.com/

Thank You,
Wesley

```html
<!DOCTYPE html>
<html lang="en">
<head>
<meta charset="utf-8">
<title>BRC Trifold</title>
<link rel="stylesheet" href="https://fonts.googleapis.com/css2?family=Playfair+Display:wght@400;700&family=Open+Sans:wght@400;600;700&display=swap">
<style>
:root{
  --maroon:#7a2d33;
  --maroon-dark:#5e2227;
  --paper:#ffffff;
  --ink:#3b3b3b;
  --muted:#8b8b8b;
  --stage:#e4e4e4;
  --sky:#9fb6c9;
  --lawn:#6f8a4c;
  --brick:#a07d66;
  --room:#cfc8bf;
  --tile:#e8e4de;
}
*{box-sizing:border-box;margin:0;padding:0}
html,body{width:865px;height:1200px;overflow:hidden;background:var(--stage)}
body{position:relative;font-family:"Open Sans",sans-serif;color:var(--ink)}
.sheet{position:absolute;left:42px;width:780px;height:540px;background:var(--paper);box-shadow:0 4px 14px rgba(0,0,0,.18);overflow:hidden}
.sheet--outside{top:30px}
.sheet--inside{top:630px}
.panel{position:absolute;top:0;width:260px;height:540px;overflow:hidden}
.panel--1{left:0}.panel--2{left:260px}.panel--3{left:520px}
.fold{position:absolute;top:0;width:1px;height:540px;background:rgba(0,0,0,.06)}
.photo{position:absolute}
.photo--house{background:linear-gradient(180deg,var(--sky) 0%,#c9d6de 40%,var(--brick) 62%,var(--lawn) 78%,#55703a 100%)}
.photo--interior{background:linear-gradient(160deg,#f1eee9 0%,var(--room) 55%,#a89f94 100%)}
.photo--kitchen{background:linear-gradient(180deg,#f4f2ef 0%,var(--tile) 50%,#b9b2a8 100%)}
.photo--bath{background:linear-gradient(170deg,#eef0f0 0%,#d7d9d8 50%,#a9a7a2 100%)}
.band{position:absolute;background:var(--maroon)}
.serif{font-family:"Playfair Display",serif}
.brand{display:flex;align-items:center;gap:8px}
.brand__mark{width:22px;height:22px;background:var(--maroon)}
.brand__name{font-family:"Open Sans",sans-serif;font-weight:700;font-size:15px;letter-spacing:2px;color:var(--maroon)}
.small{font-size:8.5px;line-height:1.5}
.heading{font-family:"Playfair Display",serif;font-weight:700;color:var(--maroon)}
.veteran{position:absolute;left:20px;top:22px;display:flex;align-items:center;gap:8px}
.veteran__badge{width:30px;height:30px;border-radius:50%;background:var(--maroon)}
.veteran__label{font-size:8px;font-weight:700;letter-spacing:1px;color:var(--maroon)}
.intro-box{position:absolute;left:20px;top:70px;width:220px;height:170px;background:var(--maroon);color:#fff;padding:16px 14px}
.intro-box p{font-size:9px;line-height:1.55}
.intro-box p + p{margin-top:8px}
.center{text-align:center}
.badges{display:flex;justify-content:center;gap:10px}
.badge{width:24px;height:24px;border-radius:50%;background:#c8c8c8}
.contact-line{display:flex;align-items:center;justify-content:center;gap:6px;font-size:10px;font-weight:700;color:var(--maroon)}
.service{position:absolute}
.service h3{font-family:"Playfair Display",serif;font-size:12px;color:var(--maroon);margin-bottom:3px}
.service p{font-size:7.5px;line-height:1.5;color:var(--ink)}
.tag{position:absolute;background:var(--maroon);color:#fff;font-family:"Playfair Display",serif;font-size:11px;padding:4px 10px}
</style>
</head>
<body>

<!-- Outside of the trifold -->
<section class="sheet sheet--outside">
  <div class="panel panel--1">
    <div class="veteran">
      <div class="veteran__badge"></div>
      <span class="veteran__label">VETERAN OWNED</span>
    </div>
    <div class="intro-box">
      <p>Proudly veteran owned and operated, we bring the same discipline and care to every roof and room we touch.</p>
      <p>Our crews treat your home like their own, from the first inspection to the final walkthrough.</p>
      <p>Honest quotes, clean job sites and work we stand behind for years.</p>
    </div>
    <div class="photo photo--house" role="img" aria-label="Photo of a brick ranch house with a green lawn" style="left:0;top:320px;width:260px;height:220px;clip-path:polygon(0 18%,100% 0,100% 100%,0 100%)"></div>
  </div>

  <div class="panel panel--2">
    <div class="photo photo--interior" role="img" aria-label="Photo of a finished home exterior" style="left:0;top:0;width:260px;height:120px;clip-path:polygon(0 0,100% 0,100% 70%,0 100%)"></div>
    <div class="brand" style="position:absolute;left:70px;top:140px">
      <div class="brand__mark"></div><span class="brand__name">BRELLMONT</span>
    </div>
    <div class="center" style="position:absolute;left:0;top:185px;width:260px">
      <p class="heading" style="font-size:20px">SINCE 1990</p>
      <p class="small" style="margin-top:4px;font-weight:600;letter-spacing:1px">LOCALLY OWNED &amp; OPERATED</p>
      <p class="small" style="color:var(--muted)">ROOFING &bull; SIDING &bull; REMODELING</p>
      <p class="serif" style="font-size:14px;color:var(--maroon);margin-top:16px">Let's Chat</p>
      <div class="contact-line" style="margin-top:4px">
        <svg width="10" height="10" viewBox="0 0 24 24"><path fill="#7a2d33" d="M6.6 10.8a15 15 0 006.6 6.6l2.2-2.2a1 1 0 011-.25 11.4 11.4 0 003.6.6 1 1 0 011 1V20a1 1 0 01-1 1A17 17 0 013 4a1 1 0 011-1h3.5a1 1 0 011 1 11.4 11.4 0 00.6 3.6 1 1 0 01-.25 1z"/></svg>
        (555) 014-2290
      </div>
      <p class="small" style="margin-top:6px;color:var(--muted)">1482 Harlow Ridge Rd, Brellmont<br>brellmontroofingandconstruction.com</p>
    </div>
    <div class="badges" style="position:absolute;left:0;top:400px;width:260px">
      <span class="badge"></span><span class="badge"></span><span class="badge"></span><span class="badge"></span>
    </div>
  </div>

  <div class="panel panel--3">
    <div class="photo photo--house" role="img" aria-label="Photo of a two-story home with a new roof" style="left:0;top:0;width:260px;height:140px"></div>
    <div class="band" style="left:0;top:110px;width:260px;height:40px;clip-path:polygon(0 70%,100% 0,100% 30%,0 100%)"></div>
    <div class="brand" style="position:absolute;left:70px;top:165px">
      <div class="brand__mark"></div><span class="brand__name">BRELLMONT</span>
    </div>
    <p class="small" style="position:absolute;left:24px;top:205px;width:212px;color:var(--ink)">From the roof over your head to the rooms you live in, we build, repair and remodel with quality materials and care for every detail in your home.</p>
    <div class="photo photo--kitchen" role="img" aria-label="Photo of a bright remodeled kitchen" style="left:0;top:300px;width:260px;height:240px;clip-path:polygon(0 20%,100% 0,100% 100%,0 100%)"></div>
    <div class="band" style="left:0;top:290px;width:260px;height:40px;clip-path:polygon(0 100%,100% 0,100% 30%,0 80%)"></div>
  </div>
  <span class="fold" style="left:260px"></span><span class="fold" style="left:520px"></span>
</section>

<!-- Inside of the trifold -->
<section class="sheet sheet--inside">
  <div class="panel panel--1">
    <div class="band" style="left:0;top:0;width:260px;height:130px;clip-path:polygon(0 0,100% 0,100% 65%,0 100%)"></div>
    <h2 class="serif" style="position:absolute;left:18px;top:22px;width:220px;color:#fff;font-size:17px;line-height:1.25">Home Construction &amp; Remodeling Services</h2>
    <p style="position:absolute;left:18px;top:72px;width:200px;color:#fff;font-size:7.5px;line-height:1.5">Everything your home needs, handled by one trusted local team.</p>
    <div class="service" style="left:18px;top:150px;width:110px">
      <h3>Roofing</h3>
      <p>Shingle replacement, leak repair and full tear-offs done right.</p>
    </div>
    <div class="photo photo--house" role="img" aria-label="Photo of a roof being installed" style="left:135px;top:140px;width:125px;height:110px;clip-path:polygon(15% 0,100% 0,100% 100%,0 100%)"></div>
    <div class="photo photo--house" role="img" aria-label="Photo of a house with new siding" style="left:0;top:270px;width:125px;height:120px;clip-path:polygon(0 0,100% 0,85% 100%,0 100%)"></div>
    <div class="service" style="left:138px;top:280px;width:110px">
      <h3>Siding</h3>
      <p>Durable siding in colors that fit your style and budget.</p>
    </div>
    <div class="service" style="left:18px;top:410px;width:225px">
      <h3>Gutters &amp; Windows</h3>
      <p>Seamless gutters and energy efficient windows that protect and save.</p>
    </div>
  </div>

  <div class="panel panel--2">
    <div class="photo photo--interior" role="img" aria-label="Photo of a remodeled living room" style="left:0;top:0;width:260px;height:170px;clip-path:polygon(0 0,100% 0,100% 80%,0 100%)"></div>
    <div class="service" style="left:18px;top:185px;width:225px">
      <h3>Kitchens</h3>
      <p>Custom cabinets, counters and layouts designed around how you cook and gather.</p>
    </div>
    <div class="photo photo--bath" role="img" aria-label="Photo of a remodeled bathroom with a glass shower" style="left:0;top:250px;width:260px;height:150px;clip-path:polygon(0 15%,100% 0,100% 85%,0 100%)"></div>
    <div class="service" style="left:18px;top:415px;width:225px">
      <h3>Bathrooms</h3>
      <p>Walk-in showers, tile, vanities and fixtures for a space you will love.</p>
    </div>
  </div>

  <div class="panel panel--3">
    <div class="photo photo--kitchen" role="img" aria-label="Photo of a white kitchen with an island" style="left:0;top:0;width:260px;height:210px;clip-path:polygon(0 0,100% 0,100% 100%,0 80%)"></div>
    <div class="tag" style="left:20px;top:220px">Basements</div>
    <p class="small" style="position:absolute;left:20px;top:252px;width:220px">Turn unused space into a family room, office or guest suite.</p>
    <div class="photo photo--interior" role="img" aria-label="Photo of a finished basement" style="left:0;top:300px;width:260px;height:130px;clip-path:polygon(0 20%,100% 0,100% 100%,0 100%)"></div>
    <div class="brand" style="position:absolute;left:70px;top:470px">
      <div class="brand__mark"></div><span class="brand__name">BRELLMONT</span>
    </div>
  </div>
  <span class="fold" style="left:260px"></span><span class="fold" style="left:520px"></span>
</section>

</body>
</html>
```